Lorvik.no is a new website about pedagogical entrepreneurship. It's main target group is teachers. The Fjellmark Bureau for Digital Schooling and the Halvstad Agency for Classroom Affairs are leading the project.

The web page is meant to show examples of how different methods of entrepreneurship can be used pedagogical in a learning environment. The page will also support the user with examples of different teaching programs and other examples of best practice.

Pedagogical entrepreneurship is not about business and men in suits. It's a method for learning. The focus in the design should be on school, education and new ways of learning.

The final product should be motivating and engaging, but at the same time governmental and serious. We are not looking for something "flashy" and corporate-looking, but a moderate, task-focused and clean design that state quality.

We need designs for three pages:
1 - frontpage
2 - subpage ("Metoder og undervisningsopplegg")
3 - subpage ("Tavle-KOMP i Brekkvoll")

The interaction design for these three pages will be uploaded as an attachment.

We would like you to find inspiration in the following websites:
- www.skaperlund.no
- www.guldrim.no
- www.brambelquest.com
- www.tuv.no
(more will be added)

Please use the attached logo, and feel free to use this as an inspiration for the rest of the design.

Reason: We are awaiting improved designs from some designers, and need to extend the deadline a couple of days.

Target Market(s)

Teachers

Industry/Entity Type

Education

Requirements
Must have
• * Header with: Logo. Main navigation. Utility navigation. Search box.
* Footer
Should not have
• Images of men in suits.
Very strong graphical elements that stands out too much (we want it clean).

```html
<!DOCTYPE html>
<html lang="en">
<head>
<meta charset="utf-8">
<title>Lorvik – Pedagogical Entrepreneurship</title>
<link href="https://fonts.googleapis.com/css2?family=PT+Sans:wght@400;700&family=Open+Sans:wght@400;600;700&family=Russo+One&display=swap" rel="stylesheet">
<style>
:root{
  --blue:#1f86c4;
  --blue-dark:#1a5f96;
  --navy:#1c3a6b;
  --green:#6aa61d;
  --lime:#9fd13a;
  --hero-top:#6dc4ef;
  --hero-bottom:#1872aa;
  --text:#3d3d3d;
  --muted:#5a5a5a;
  --line:#d9d9d9;
  --white:#ffffff;
}
*{margin:0;padding:0;box-sizing:border-box}
html,body{width:1127px;height:1200px;overflow:hidden;background:var(--white)}
body{font-family:"Open Sans",sans-serif;color:var(--text);position:relative}
.abs{position:absolute}
a{color:inherit;text-decoration:none}

/* header */
.site-header{left:0;top:0;width:1127px;height:116px;background:linear-gradient(#ffffff,#ececec);border-bottom:1px solid #d5d5d5}
.brand{left:96px;top:30px;display:flex;align-items:center;gap:14px}
.brand-mark{width:64px;height:64px;border-radius:50%;background:var(--blue)}
.brand-name{font-family:"PT Sans",sans-serif;font-weight:700;font-size:54px;color:var(--blue);line-height:1}
.utility-nav{left:526px;top:11px;font-family:"PT Sans",sans-serif;font-size:13px;color:#555;display:flex;gap:12px}
.utility-nav .sep{color:#777}
.search{left:867px;top:8px;width:164px;height:23px;border:2px solid #e2e2e2;border-radius:12px;background:#fff;font-size:11px;color:#aaa;padding:2px 0 0 18px}
.search svg{position:absolute;right:8px;top:3px}
.main-nav{top:90px;font-family:"PT Sans",sans-serif;font-size:13px;color:#555}
.nav-home{left:516px;top:83px;width:95px;height:30px;background:linear-gradient(#44a9e0,#1a78b8);clip-path:polygon(8% 0,92% 0,100% 100%,0 100%);color:#fff;font-family:"PT Sans",sans-serif;font-size:13px;text-align:center;line-height:30px}

/* hero */
.hero{left:0;top:116px;width:1127px;height:327px;background:linear-gradient(var(--hero-top),var(--hero-bottom))}
.hero-title{left:133px;top:160px;font-family:"Russo One",sans-serif;font-size:27px;color:var(--navy);letter-spacing:.3px;text-shadow:0 0 2px #fff,0 0 2px #fff,0 0 2px #fff}
.hero-title span{color:var(--lime)}
.hero-rule{left:136px;top:214px;width:340px;border-top:1px dotted rgba(255,255,255,.7)}
.hero-lead{left:146px;top:235px;width:395px;font-size:11px;line-height:17px;color:#fff}
.hero-lead b{font-weight:700}
.hero-list{left:150px;top:302px;list-style:none;font-size:11px;color:#fff;line-height:20.7px;letter-spacing:.3px}
.hero-list li::before{content:"»";color:var(--lime);font-weight:700;margin-right:8px}
.view-more{left:153px;top:398px;font-family:"PT Sans",sans-serif;font-weight:700;font-size:14px;color:var(--lime);display:flex;align-items:center;gap:7px}
.hero-art{left:601px;top:127px;width:394px;height:310px;border-radius:40% 40% 45% 45%;background:radial-gradient(circle at 55% 60%,#ffffff 0%,#e7f3fb 45%,rgba(255,255,255,0) 72%)}

/* columns */
.col-sep{top:460px;width:10px;height:292px;background:linear-gradient(90deg,rgba(0,0,0,.07),rgba(0,0,0,0))}
.col-title{font-family:"PT Sans",sans-serif;font-size:18px;font-weight:700;color:#3a3a3a;display:flex;align-items:center;gap:10px;white-space:nowrap}
.col-title em{font-style:normal;color:var(--green)}
.small-icon{width:26px;height:24px;border-radius:4px}
.col-art{left:147px;top:521px;width:191px;height:132px;background:radial-gradient(circle,#3c9a3c 0%,#e9f3e2 70%,#fff 100%)}
.body-text{font-size:10.5px;line-height:17px;color:var(--muted)}
.body-text b{color:#333;font-weight:700}
.body-flow p{margin-bottom:8px}
.more{font-family:"PT Sans",sans-serif;font-weight:700;font-size:12.5px;color:var(--blue)}
.bullets{list-style:none;font-size:10.5px;line-height:20.7px;color:var(--muted)}
.bullets li::before{content:"";display:inline-block;width:7px;height:7px;background:var(--lime);margin-right:10px;vertical-align:1px}
.example{width:224px}
.example h4{font-size:11px;color:var(--blue);font-weight:700}
.example p{font-size:10px;line-height:17.5px;color:var(--muted);letter-spacing:.2px}
.dots{width:224px;border-top:1px dotted #999}

/* promo */
.promo{left:106px;top:784px;width:311px;height:192px;border:1px solid #dedede;border-radius:8px;background:linear-gradient(#ffffff,#ececec)}
.promo-title{left:14px;top:12px;font-family:"PT Sans",sans-serif;font-weight:700;font-size:18px;line-height:23px;color:#4a4a4a}
.promo-title em{font-style:normal;color:var(--green)}
.promo-sub{left:15px;top:83px;font-family:"PT Sans",sans-serif;font-size:14px;color:#222}
.try{left:15px;top:127px;width:140px;height:40px;border-radius:6px;background:linear-gradient(#5ab8ea,#1a77b8);color:#fff;font-family:"PT Sans",sans-serif;font-weight:700;font-size:21px;line-height:40px;padding-left:26px}
.gauge{left:157px;top:39px;width:139px;height:139px;border-radius:50%;background:radial-gradient(circle at 45% 40%,#3f7f96 0%,#1d2a33 45%,#9aa3a8 75%,#e5e7e8 100%)}

/* inspiration */
.section-title{left:444px;top:768px;font-family:"PT Sans",sans-serif;font-weight:700;font-size:20px;color:var(--blue)}
.photo{top:811px;width:181px;height:151px;background:linear-gradient(#a3a3a3 0%,#cfcfcf 35%,#7a7c7e 60%,#3b3d40 100%)}
.caption{top:967px;width:181px;font-family:"PT Sans",sans-serif;font-size:12px;color:#444;white-space:nowrap}
.arrow{top:866px;width:28px;height:44px;border-radius:6px;background:linear-gradient(#9dd6f5,#2a8acb);border:2px solid #fff;box-shadow:0 1px 3px rgba(0,0,0,.3)}

/* footer */
.site-footer{left:0;top:1018px;width:1127px;height:182px;background:linear-gradient(#6cc5f0,#1a6fa8)}
.footer-mark{left:111px;top:1031px;width:52px;height:52px;border-radius:50%;background:#fff;opacity:.9}
.footer-head{top:1038px;font-family:"PT Sans",sans-serif;font-weight:700;font-size:18px;color:#fff}
.footer-links{top:1078px;list-style:none;font-family:"PT Sans",sans-serif;font-size:13.5px;line-height:22.5px;color:#fff}
.bottom-nav{left:116px;top:1170px;display:flex;gap:22px;font-family:"PT Sans",sans-serif;font-size:12.5px;color:#fff}
.copyright{right:113px;top:1170px;font-family:"PT Sans",sans-serif;font-size:12.5px;color:#fff}
</style>
</head>
<body>

<header class="site-header abs">
  <div class="brand abs"><span class="brand-mark"></span><span class="brand-name">Lorvik</span></div>
  <nav class="utility-nav abs"><a href="#">Best Practice Schools</a><span class="sep">|</span><a href="#">Lorvikometer</a><span class="sep">|</span><a href="#">About lorvik.no</a></nav>
  <div class="search abs">Search Here
    <svg width="18" height="14" viewBox="0 0 18 14"><circle cx="6" cy="6" r="4.5" fill="none" stroke="#8cc63f" stroke-width="2"/><path d="M9.5 8.5l6 4" stroke="#8cc63f" stroke-width="2.5"/></svg>
  </div>
  <a class="nav-home abs" href="#">Home</a>
  <a class="main-nav abs" style="left:623px" href="#">Services</a>
  <a class="main-nav abs" style="left:713px" href="#">Projects</a>
  <a class="main-nav abs" style="left:796px" href="#">Course</a>
  <a class="main-nav abs" style="left:880px" href="#">About Us</a>
  <a class="main-nav abs" style="left:976px" href="#">Contact</a>
</header>

<section class="hero abs"></section>
<h1 class="hero-title abs">PEDAGOGICAL <span>ENTREPRENEURSHIP</span></h1>
<div class="hero-rule abs"></div>
<p class="hero-lead abs"><b>Lorem Ipsum is simply dummy text of the printing and typesetting industry. Lorem</b> Ipsum has been the industry's standard dummy text ever since</p>
<ul class="hero-list abs">
  <li>lorum ipsum is simply a dunny text</li>
  <li>Better management of operating costs</li>
  <li>lorum ipsum is dummy text</li>
  <li>lorvik entreprenorielle metodere</li>
</ul>
<a class="view-more abs" href="#">View more
  <svg width="17" height="17" viewBox="0 0 17 17"><circle cx="8.5" cy="8.5" r="7.5" fill="none" stroke="#fff" stroke-width="1.5"/><path d="M7 5l4 3.5-4 3.5" fill="none" stroke="#fff" stroke-width="1.5"/></svg>
</a>
<div class="hero-art abs" role="img" aria-label="Illustration of a cheerful schoolboy with a chalkboard, graduation cap, books and a pencil on a cloud"></div>

<!-- columns -->
<div class="col-sep abs" style="left:413px"></div>
<div class="col-sep abs" style="left:753px"></div>

<h2 class="col-title abs" style="left:113px;top:480px"><span class="small-icon" style="background:var(--blue);border-radius:50%"></span><span><em>Pedagocical</em> Enterpreneurship</span></h2>
<div class="col-art abs" role="img" aria-label="Illustration of a green chalkboard with letters, a globe, an apple and school supplies"></div>
<p class="body-text abs" style="left:119px;top:668px;width:272px">Lorem Ipsum is simply dummy text of the printing and typesetting industry. Lorem Ipsum has been the industry's standard dummy text ever since</p>
<a class="more abs" style="left:320px;top:730px" href="#">Moreinfo[+]</a>

<h2 class="col-title abs" style="left:451px;top:480px"><span class="small-icon" style="background:#2b3a44"></span><span><em>Methods and</em> teaching plans</span></h2>
<div class="body-flow abs" style="left:446px;top:523px;width:292px">
  <p class="body-text"><b>Lorem Ipsum is simply dummy text of the printing and typesetting industry. Lorem</b> Ipsum has been the industry's standard dummy text ever since</p>
  <p class="body-text">Lorem Ipsum is simply dummy text of the printing and typesetting industry.</p>
</div>
<ul class="bullets abs" style="left:450px;top:636px">
  <li>lorum ipsum is simply a dummy text</li>
  <li>dummy text only.</li>
  <li>Filling gaps in technical expertise</li>
  <li>lorum ipsum is simply a dummy text</li>
</ul>
<a class="more abs" style="left:662px;top:730px" href="#">Moreinfo[+]</a>

<h2 class="col-title abs" style="left:777px;top:480px"><span class="small-icon" style="background:#333"></span><span><em>Good</em> Examples</span></h2>
<div class="example abs" style="left:787px;top:526px"><h4>lorum ipsum: InkLane is simply</h4><p>from Around the Web Favorite Links from Around the Web April 2nd-6th</p></div>
<div class="dots abs" style="left:787px;top:585px"></div>
<div class="example abs" style="left:787px;top:596px"><h4>lorum ipsum: InkLane is simply</h4><p>from Around the Web Favorite Links from Around the Web April 2nd-6th</p></div>
<div class="dots abs" style="left:787px;top:655px"></div>
<div class="example abs" style="left:787px;top:668px"><h4>lorum ipsum: InkLane is simply</h4><p>from Around the Web Favorite Links from Around the Web April 2nd-6th</p></div>
<a class="more abs" style="left:934px;top:730px" href="#">Moreinfo[+]</a>

<!-- promo -->
<aside class="promo abs">
  <h3 class="promo-title abs"><em>Are you working</em> Enterpreneurship<br>like this ?</h3>
  <p class="promo-sub abs">Try the lorvikometer</p>
  <a class="try abs" href="#">Try Now</a>
  <div class="gauge abs" role="img" aria-label="Round glossy gauge icon with a dropper"></div>
</aside>

<!-- inspiration -->
<h2 class="section-title abs">Inspiration</h2>
<div class="photo abs" style="left:443px" role="img" aria-label="Photo of a white school building under a grey sky"></div>
<div class="photo abs" style="left:638px" role="img" aria-label="Photo of a white school building under a grey sky"></div>
<div class="photo abs" style="left:833px" role="img" aria-label="Photo of a white school building under a grey sky"></div>
<p class="caption abs" style="left:449px">Tavle-KOMP at Brekkvoll school</p>
<p class="caption abs" style="left:647px">Tavle-KOMP at Brekkvoll school</p>
<p class="caption abs" style="left:842px">Tavle-KOMP at Brekkvoll school</p>
<a class="arrow abs" style="left:431px" href="#" aria-label="Previous"><svg width="24" height="40" viewBox="0 0 24 40"><path d="M15 11l-8 9 8 9" fill="none" stroke="#fff" stroke-width="4"/></svg></a>
<a class="arrow abs" style="left:995px" href="#" aria-label="Next"><svg width="24" height="40" viewBox="0 0 24 40"><path d="M9 11l8 9-8 9" fill="none" stroke="#fff" stroke-width="4"/></svg></a>

<!-- footer -->
<footer class="site-footer abs"></footer>
<div class="footer-mark abs"></div>
<h3 class="footer-head abs" style="left:178px">Pedagogical Enterpreneurship</h3>
<h3 class="footer-head abs" style="left:491px">Methods</h3>
<h3 class="footer-head abs" style="left:650px">Gode Eksempler</h3>
<h3 class="footer-head abs" style="left:864px">Teaching Plans</h3>
<ul class="footer-links abs" style="left:181px"><li>Best practice school</li><li>About Pedagogical</li><li>Lorvikometer</li></ul>
<ul class="footer-links abs" style="left:490px"><li>Best practice school</li><li>About Pedagogical</li><li>Lorvikometer</li></ul>
<ul class="footer-links abs" style="left:654px"><li>Best practice school</li><li>About Pedagogical</li><li>Lorvikometer</li></ul>
<ul class="footer-links abs" style="left:867px"><li>Best practice school</li><li>About Pedagogical</li><li>Lorvikometer</li></ul>
<nav class="bottom-nav abs"><a href="#">Home</a><span>|</span><a href="#">Services</a><span>|</span><a href="#">Projects</a><span>|</span><a href="#">Course</a><span>|</span><a href="#">About Us</a><span>|</span><a href="#">Contact Us</a></nav>
<p class="copyright abs">Copyright @ 2012 Lorvik.com . All Right Reserved</p>

</body>
</html>
```